Massage Certificate Design that is Elegant, Modern, Hip with a "Pop"

We need a massage certificate for our Chiropractic office. Our brand feel is modern, clean, hip, and bold. Something that has some "pop" to it and that is different. We play dance music on Fridays, we care for kids and families, and provide vitality care, not just about neck and back pain. We would like to see a design that incorporates our logo along with a burnt orange accent color, tan, white, and black. We attached a sample certificate. On one side we would like to have it designate the massage price of $50, a space to write in who the certificate is for, who it is from, a space to write in an expiration date. On the back of the certificate we would like to have the office contact info. 4173 W. Marlow Lane, C204, Larkspur Hills, AZ 85099. A map of the location.
Phone: (480) 731-2946
Facebook
Twitter

Target Market(s)

Moms, Wellness Minded, Vitality Focused, Looking for reducing stress and muscle stiffness

Industry/Entity Type

Health And Wellness

Colors
f37122
000000
fefefe

Requirements
Must have
• Burnt orange accent color, tan, black, and white colors used.

```html
<!DOCTYPE html>
<html lang="en">
<head>
<meta charset="utf-8">
<title>Lumen Arc Chiropractic – Massage Certificate</title>
<link rel="stylesheet" href="https://fonts.googleapis.com/css2?family=Open+Sans:wght@400;600&family=Orbitron:wght@700&display=swap">
<style>
  :root {
    --backdrop: #6d6e71;
    --ink: #000000;
    --paper: #fefefe;
    --orange: #f7941d;
    --tan-light: #ebe6da;
    --tan-dark: #ddd5c3;
    --rule: #1a1a1a;
  }
  * { box-sizing: border-box; margin: 0; padding: 0; }
  html, body { width: 1200px; height: 927px; overflow: hidden; }
  body {
    position: relative;
    background: var(--backdrop);
    font-family: "Open Sans", Arial, sans-serif;
  }
  .card { position: absolute; left: 135px; width: 930px; }
  .card--front { top: 36px; height: 413px; background: var(--paper); }
  .card--back { top: 478px; height: 412px; background: var(--ink); }

  .brand-name {
    position: absolute; color: var(--paper); font-weight: 400;
    white-space: nowrap; line-height: 1;
  }

  /* front */
  .brand-panel {
    position: absolute; left: 0; top: 0; width: 238px; height: 100%;
    background: var(--ink);
  }
  .brand-panel .brand-name { right: 20px; top: 358px; font-size: 16px; }
  .fold-shadow {
    position: absolute; left: 251px; top: 0; width: 18px; height: 100%;
    background: linear-gradient(to right, rgba(0,0,0,0.18), rgba(0,0,0,0));
  }
  .top-band {
    position: absolute; left: 251px; top: 0; right: 0; height: 26px;
    background: var(--orange);
  }
  .divider {
    position: absolute; left: 584px; top: 27px; width: 2px; height: 267px;
    background: var(--rule);
  }
  .write-line {
    position: absolute; height: 2px; width: 301px; background: var(--rule);
  }
  .expiry {
    position: absolute; left: 271px; top: 363px;
    display: flex; align-items: flex-end;
    font-size: 18px; line-height: 24px; color: var(--rule); white-space: nowrap;
  }
  .expiry-line {
    display: inline-block; width: 218px; height: 20px;
    border-bottom: 1.5px solid var(--rule);
  }
  .foot-band {
    position: absolute; left: 651px; right: 0; top: 365px; height: 20px;
    background: var(--orange);
  }

  /* back */
  .map-area {
    position: absolute; left: 0; top: 0; width: 568px; height: 353px;
    background: linear-gradient(135deg, var(--tan-light), var(--tan-dark));
  }
  .map-frame-right {
    position: absolute; left: 568px; top: 0; width: 14px; height: 369px;
    background: var(--orange);
  }
  .map-frame-bottom {
    position: absolute; left: 0; top: 353px; width: 582px; height: 16px;
    background: var(--orange);
  }
  .address-bar {
    position: absolute; left: 0; top: 369px; width: 100%; height: 43px;
    background: var(--ink); color: var(--paper);
    font-size: 20px; font-weight: 600; padding-left: 29px; line-height: 43px;
    white-space: nowrap;
  }
  .phone {
    position: absolute; left: 582px; top: 0; width: 348px; height: 88px;
    color: var(--paper); font-size: 25px; font-weight: 600;
    text-align: center; line-height: 84px; white-space: nowrap;
  }
  .price-band {
    position: absolute; left: 582px; top: 88px; width: 348px; height: 52px;
    background: var(--orange); color: var(--paper);
    font-family: "Orbitron", "Open Sans", sans-serif; font-weight: 700;
    text-align: center; line-height: 52px; font-size: 40px;
  }
  .price-band .cents { font-size: 22px; }
  .card--back .brand-name { left: 682px; top: 334px; font-size: 20px; }
  .social {
    position: absolute; top: 228px; width: 50px; height: 50px;
    border-radius: 50%; background: var(--paper);
  }
</style>
</head>
<body>

<section class="card card--front" aria-label="Massage certificate front">
  <div class="brand-panel">
    <p class="brand-name">Lumen Arc Chiropractic</p>
  </div>
  <div class="fold-shadow"></div>
  <div class="top-band"></div>
  <div class="divider"></div>
  <div class="write-line" style="left:271px; top:118px;"></div>
  <div class="write-line" style="left:271px; top:205px;"></div>
  <div class="write-line" style="left:271px; top:292px;"></div>
  <div class="write-line" style="left:599px; top:118px;"></div>
  <div class="write-line" style="left:599px; top:205px;"></div>
  <div class="write-line" style="left:599px; top:292px;"></div>
  <p class="expiry">Expiration Date:<span class="expiry-line"></span></p>
  <div class="foot-band"></div>
</section>

<section class="card card--back" aria-label="Massage certificate back">
  <div class="map-area" role="img" aria-label="Street map showing the office location"></div>
  <div class="map-frame-right"></div>
  <div class="map-frame-bottom"></div>
  <p class="phone">Phone: (480) 731-2946</p>
  <p class="price-band">$50<span class="cents">.00</span></p>
  <div class="social" style="left:784px;" role="img" aria-label="Social profile link"></div>
  <div class="social" style="left:852px;" role="img" aria-label="Social profile link"></div>
  <p class="brand-name">Lumen Arc Chiropractic</p>
  <p class="address-bar">A: 4173 W. Marlow Lane, C204, Larkspur Hills, AZ 85099</p>
</section>

</body>
</html>
```